Local massage therapist needs some new marketing material

Hi there! I am a massage therapist here in Denver, CO in Brindle Hollow(shopping and art district) of the city. My business is called Lunora Massage of Denver. My practice has an eastern influence and I do reflexology, thai massage and use Chinese herbs, etc. I know all my clients and pay close attention to details. I am also very respectful of tradition and it shows in how I work. I tend to like modern, clean, fun, Asian designs. I am wanting a new business card and brochure. I have a logo and branding for my business that I want used in the design. Currently, the sign for my building is purple and I think my logo was designed to be purple. I will attach pictures of it and can send whatever files are necessary so it can be integrated into the brochure, etc. I like the purple but open to using other colors as well. Thanks!
My website is lunoramassagestudio.example where info can be gathered about me and services/fees for brochure.
Updates

Just increased budget. Please see new feedback in discussion thread.

Thanks!

                                       HEY ALL,

Just wanted to let you know that I made a change to my website. It is on the Prices Page. I no longer have the frequent  flyer prices but I added discounts. Let me know if you have any questions. Thanks so much!

Target Market(s)

healthy, urban, educated, upper middle class, yogis

Industry/Entity Type

Marketing

Requirements
Must have
• logo stays purple
Should not have
• not too busy

```html
<!DOCTYPE html>
<html lang="en">
<head>
<meta charset="UTF-8">
<title>Lunora Massage of Denver – Brochure Spread</title>
<link rel="stylesheet" href="https://fonts.googleapis.com/css2?family=Josefin+Sans:wght@300;400;600&family=Montserrat:ital,wght@0,400;0,600;1,400&display=swap">
<style>
  :root {
    --purple: #6a2a90;
    --lime: #b9d437;
    --white: #ffffff;
    --page-bg: #c9c9c9;
  }
  * { box-sizing: border-box; margin: 0; padding: 0; }
  html, body { width: 1200px; height: 848px; overflow: hidden; background: var(--page-bg); }
  body { font-family: "Montserrat", sans-serif; color: var(--white); }

  .spread { position: relative; width: 1200px; height: 848px; display: flex; }
  .page { position: relative; width: 600px; height: 848px; overflow: hidden; }
  .page--prices { background: var(--white); }
  .page--methods { background: var(--purple); }

  .photo { position: absolute; }
  .photo--green { background: linear-gradient(135deg, #5f8f2e, #2f5a1c); }
  .photo--spa { background: linear-gradient(135deg, #f4f1ec, #e3dbd0); }
  .photo--skin { background: linear-gradient(135deg, #e3b497, #7d9c4a); }
  .photo--warm { background: linear-gradient(135deg, #c99a6e, #5b3d28); }

  .price-panel {
    position: absolute; left: 200px; top: 200px; width: 400px; height: 440px;
    background: var(--purple); padding: 22px 20px 0 28px; overflow: hidden;
  }
  .price-title {
    font-family: "Josefin Sans", sans-serif; font-weight: 300;
    font-size: 40px; letter-spacing: 2px; color: var(--lime); line-height: 1;
    margin-bottom: 16px;
  }
  .price-group { margin-bottom: 16px; }
  .price-group-title { font-weight: 600; font-size: 11.5px; color: var(--lime); margin-bottom: 2px; }
  .price-row {
    display: flex; font-size: 11px; line-height: 1.32;
    border-bottom: 1px dotted rgba(255,255,255,0.6); padding: 2px 0 1px;
  }
  .price-row .item { width: 208px; flex: none; padding-right: 6px; }
  .price-row .amount { flex: 1; color: var(--lime); white-space: nowrap; }
  .price-row--tall .item { width: 170px; margin-right: 38px; }
  .price-note { font-style: italic; font-size: 10.5px; line-height: 1.35; color: var(--lime); }

  .methods-heading {
    position: absolute; left: 30px; top: 40px; width: 560px;
    font-family: "Josefin Sans", sans-serif; font-weight: 600;
    font-size: 21px; letter-spacing: 1px; color: var(--lime);
  }
  .treats-heading {
    position: absolute; left: 30px; top: 318px;
    font-family: "Josefin Sans", sans-serif; font-weight: 600;
    font-size: 24px; color: var(--lime);
  }
  .method { position: absolute; left: 30px; width: 410px; }
  .method h3 { font-size: 12.5px; font-weight: 600; color: var(--lime); margin-bottom: 2px; }
  .method p { font-size: 11.3px; line-height: 1.38; }

  .thumb {
    position: absolute; left: 455px; width: 118px; height: 76px;
    border: 3px solid var(--lime);
  }
</style>
</head>
<body>
<main class="spread">
  <section class="page page--prices">
    <div class="photo photo--green" style="left:0;top:0;width:200px;height:200px" role="img" aria-label="Woman relaxing with a herbal compress massage"></div>
    <div class="photo photo--spa" style="left:200px;top:0;width:200px;height:200px" role="img" aria-label="Incense bowl and white frangipani flowers"></div>
    <div class="photo photo--skin" style="left:400px;top:0;width:200px;height:200px" role="img" aria-label="Facial massage with candles and rolled towel"></div>
    <div class="photo photo--spa" style="left:0;top:200px;width:200px;height:220px" role="img" aria-label="Mortar with herbs and massage oil bottles"></div>
    <div class="photo photo--skin" style="left:0;top:420px;width:200px;height:220px" role="img" aria-label="Back massage in a green garden setting"></div>
    <div class="photo photo--spa" style="left:0;top:640px;width:200px;height:208px" role="img" aria-label="Herbal compress, mortar and oils"></div>
    <div class="photo photo--green" style="left:200px;top:640px;width:200px;height:208px" role="img" aria-label="Relaxing head massage with flower"></div>
    <div class="photo photo--spa" style="left:400px;top:640px;width:200px;height:208px" role="img" aria-label="Herbal compress, soaps and frangipani"></div>

    <div class="price-panel">
      <h2 class="price-title">PRICE LIST</h2>
      <div class="price-group">
        <h4 class="price-group-title">Standard Prices</h4>
        <div class="price-row"><span class="item">1 Hour Massage</span><span class="amount">$50</span></div>
        <div class="price-row"><span class="item">1-1/2 Hour Massage</span><span class="amount">$65</span></div>
        <div class="price-row"><span class="item">2 Hour Massage</span><span class="amount">$80</span></div>
        <div class="price-row"><span class="item">1-1/2 Hour Seasonal Massage</span><span class="amount">$75</span></div>
        <div class="price-row price-row--tall"><span class="item">Add: Fire Cupping, Hot Stones, Thai Herbal Compress or Reflexology</span><span class="amount">$10 each</span></div>
        <div class="price-row"><span class="item">Cancellation Fee*</span><span class="amount">$25 for each hour booked</span></div>
      </div>
      <div class="price-group">
        <h4 class="price-group-title">Frequent Client Prices</h4>
        <div class="price-row"><span class="item">Twice-Monthly: 1 Hour Massage</span><span class="amount">$45</span></div>
        <div class="price-row"><span class="item">Twice-Monthly: 1-1/2 Hour Massage</span><span class="amount">$60</span></div>
        <div class="price-row"><span class="item">Twice-Monthly: 2 Hour Massage</span><span class="amount">$75</span></div>
        <div class="price-row"><span class="item">Weekly Plan: 1 Hour Massage</span><span class="amount">$40</span></div>
        <div class="price-row"><span class="item">Weekly Plan: 1-1/2 Hour Massage</span><span class="amount">$55</span></div>
        <div class="price-row"><span class="item">Weekly Plan: 2 Hour Massage</span><span class="amount">$70</span></div>
      </div>
      <p class="price-note">* 24 Hour Cancelation Policy applies to all Massage.<br>Prices are subject to change. Notice will be given.</p>
    </div>
  </section>

  <section class="page page--methods">
    <h2 class="methods-heading">WE OFFER A VARIETY OF MASSAGE METHODS.</h2>

    <article class="method" style="top:84px">
      <h3>Blend Massage</h3>
      <p>Blend Massage incorporates all techniques into one fully restorative and therapeutic session. Enjoy the benefits of soothing Swedish strokes, attention to Thai Sen lines, gentle stretching and deep pressure to relieve accumulated muscle tension and stress. This is the most popular modality.</p>
    </article>
    <div class="thumb photo--skin" style="top:84px" role="img" aria-label="Back massage"></div>

    <article class="method" style="top:186px">
      <h3>Prenatal Bliss</h3>
      <p>Prenatal massage has been found to reduce stress, decrease swelling in the arms and legs, and relieve aches and pains in muscles and joints. Not only can massage be physically beneficial, but the human touch can be comforting and provide emotional support during pregnancy. Massage therapy has been found to reduce anxiety and depression. Massage is best to start during the second trimester.</p>
    </article>
    <div class="thumb photo--skin" style="top:180px" role="img" aria-label="Gentle prenatal massage"></div>

    <h2 class="treats-heading">Extra Massage Treats</h2>

    <article class="method" style="top:356px">
      <h3>Chinese Fire Cupping</h3>
      <p>Cupping Method that uses glass cups to create a vacuum on the skin of the back. The suction penetrates deep into the tissues, allowing them to relax and release toxins. It triggers the lymphatic system, clears the blood vessels, loosens tight muscles, and stimulates the skin.</p>
    </article>
    <div class="thumb photo--warm" style="top:290px" role="img" aria-label="Fire cupping treatment"></div>

    <article class="method" style="top:452px">
      <h3>Hot Stones</h3>
      <p>Hot stones (local basalt Colorado rocks) incorporates the use of smooth heated stones for a deeply soothing and relaxing experience. The stones are either used as part of a traditional swedish session or placed along specific areas of muscle tension to reduce discomfort and increase circulation. A nice treat after a long day or during the winter season.</p>
    </article>
    <div class="thumb photo--warm" style="top:386px" role="img" aria-label="Hot stone massage"></div>

    <article class="method" style="top:560px">
      <h3>Reflexology</h3>
      <p>A modality focused on the feet. It is a non-invasive way to work the entire body system. Pressure is applied to various reflexes on the foot in order to promote balance and healing in the body. Certain areas of the foot correspond to organs and specific parts of the body. Reflexology helps to clear blocked energy, balance emotions and relax the body.</p>
    </article>
    <div class="thumb photo--spa" style="top:482px" role="img" aria-label="Foot reflexology"></div>

    <article class="method" style="top:668px">
      <h3>Thai Herbal Compress</h3>
      <p>Hand-made herbal compresses imported from Thailand make for a truly delightful and unique experience. The steamed herbal compress is applied directly to the body and helps relieve sore muscles while the aroma soothes the mind.</p>
    </article>
    <div class="thumb photo--warm" style="top:578px" role="img" aria-label="Thai herbal compress treatment"></div>
  </section>
</main>
</body>
</html>
```